Wix Commerce Site for Gas Fireplace & Heater Smartphone Controller

Our company 'zKarvel' makes and sells only 2 products (so far). A device that lets you control your gas fireplace or in-wall gas heater via bluetooth app on your smartphone.
We have a Wix site with a store that has our 2 products in it now, but would like a whole new design created specifically to market and sell these devices direct to consumer from our site. Existing site is getzkarvel.example
The only thing we are married to is the logo image, but everything else can be wiped clean. We have a few product images and some images/video of us as we built the prototypes and our own manufacturing process if incorporating them improves the sales pitch. Totally fine to leave it all out as well. We will need a gallery type page that we can add instructional video to of how to install the product and such once we get better videos produced. We are a family owned and operated business that has hand built every piece of this product ourselves from designing and assembling the electronics to coding the firmware and applications and even including 3D printing the cases for the initial production run (we are setting up our own injection mold system now to make future cases faster from locally recycled plastics.
We plan to stay on the Wix Pro plan so will need a site built that we can just drop in to our existing account.
The goal is to market 1 version as the "Gas Fireplace" controller and the other as the "In-Wall Gas Heater" controller.
I have included Screenshots from the Android and iOS apps that control the devices as well as a few other random pics that may or may not be useful, but let you see visually the types of devices they control so you can find better stock images to use as necessary. Also are a couple videos that are of low production value and will be remade more professionally soon as well.
I welcome any and all questions that will aid in design and will be as responsive as possible to design submissions.
links to our apps on the google play and apple store are nice to have somewhere as well.

```html
<!DOCTYPE html>
<html lang="en">
<head>
<meta charset="utf-8">
<title>zKarvel — Smart Control for Gas Fireplaces & Wall Heaters</title>
<link href="https://fonts.googleapis.com/css2?family=Lato:wght@300;400;700&family=Questrial&display=swap" rel="stylesheet">
<style>
:root{
  --navy:#1c2a4c;
  --navy-deep:#17223f;
  --blue:#3f8ff0;
  --orange:#d98a3a;
  --gold:#d6a83c;
  --red:#b9363a;
  --ink:#222;
  --body:#555;
  --muted:#8a8a8a;
  --grey-band:#e5e6ea;
  --white:#fff;
}
*{box-sizing:border-box;margin:0;padding:0}
html,body{width:1200px;height:5025px;overflow:hidden}
body{font-family:'Lato',sans-serif;color:var(--body);background:var(--white);position:relative}
.abs{position:absolute}
.eyebrow{font-family:'Lato',sans-serif;font-size:11px;letter-spacing:9px;color:var(--ink);text-transform:uppercase}
.section-title{font-family:'Questrial',sans-serif;font-size:35px;color:var(--ink);text-transform:uppercase;font-weight:400;line-height:1.2}
.rule{height:2px;width:82px;background:var(--ink)}
.copy{font-size:14px;line-height:25px;color:var(--body);font-weight:400}
.btn-outline{display:inline-block;border:1.5px solid var(--blue);border-radius:22px;color:var(--blue);font-size:10px;letter-spacing:.5px;padding:11px 21px;text-transform:uppercase}
.placeholder{border-radius:2px}

/* header */
.hero{top:0;left:0;width:1200px;height:663px;overflow:hidden}
.nav{top:44px;left:0;width:1200px;height:40px}
.brand{display:flex;align-items:center;gap:10px;color:var(--white);font-family:'Questrial',sans-serif;font-size:26px}
.brand-dot{width:24px;height:24px;border-radius:50%;background:var(--orange)}
.nav .brand{position:absolute;left:74px;top:2px}
.nav-links{position:absolute;left:545px;top:8px;display:flex;font-size:13px;color:#c9cfdc}
.nav-links span{margin-right:38px}
.nav-links .active{color:var(--white);position:relative}
.nav-links .active::after{content:"";position:absolute;left:0;right:0;bottom:-15px;height:2px;background:var(--white)}
.hero h1{top:225px;left:111px;width:640px;font-family:'Questrial',sans-serif;font-weight:400;font-size:40px;line-height:52px;color:var(--white);white-space:nowrap}
.hero-btn{top:453px;left:111px;width:268px;height:56px;border-radius:28px;background:var(--blue);color:var(--white);font-size:12px;letter-spacing:.3px;display:flex;align-items:center;justify-content:center;gap:10px}

/* about */
.about-text{top:800px;left:680px;width:390px}
.about-text .section-title{margin-top:14px}
.about-text .copy{margin-top:42px}
.about-text .copy + .copy{margin-top:20px}
.about-text .btn-outline{margin-top:36px}

/* products */
.center-head{left:0;width:1200px;text-align:center}
.center-head .rule{margin:14px auto 0}
.product{width:284px}
.product .thumb{width:284px;height:256px;position:relative}
.heart{position:absolute;top:12px;right:12px;width:22px;height:22px;border-radius:50%;background:rgba(255,255,255,.85)}
.product .name{margin-top:20px;text-align:center;font-size:14px;color:#555}
.product .price{margin-top:34px;text-align:center;font-size:20px;color:var(--orange);font-weight:300}
.dots{top:1907px;left:590px;display:flex;gap:4px}
.dots i{width:5px;height:5px;border-radius:50%;background:#ccc;display:block}
.dots i:first-child{background:#333}

/* how it works */
.how-text{top:2210px;left:205px;width:390px}
.how-text .section-title{margin-top:12px}
.how-text .copy{margin-top:40px}
.stores{margin-top:32px;display:flex;gap:12px}
.store-badge{width:110px;height:36px;border-radius:6px;background:#111}

/* setup */
.setup-text{top:2792px;left:687px;width:390px}
.setup-text .rule{margin-top:26px}
.setup-text .copy{margin-top:40px}
.setup-text .btn-outline{margin-top:36px}
.video{top:2790px;left:123px;width:506px;height:390px;background:linear-gradient(180deg,#1f2a45,#1b2a33)}
.play{position:absolute;left:219px;top:161px;width:70px;height:70px;border-radius:50%;background:var(--white)}
.play::after{content:"";position:absolute;left:28px;top:22px;border-left:20px solid #111;border-top:13px solid transparent;border-bottom:13px solid transparent}
.video-caption{position:absolute;left:0;width:100%;top:300px;text-align:center;font-family:'Questrial',sans-serif;font-size:36px;color:rgba(255,255,255,.08)}

/* testimonials */
.testimonials{top:3291px;left:0;width:1200px;height:549px;background:linear-gradient(100deg,#b8323b 0%,#c4463a 45%,#d9883a 80%,#e3b14a 100%)}
.testimonials .eyebrow{color:rgba(255,255,255,.9)}
.testimonials .section-title{color:var(--white)}
.testimonials .rule{background:rgba(255,255,255,.8)}
.quote{position:absolute;top:210px;width:290px}
.quote .mark{font-family:Georgia,serif;font-size:36px;line-height:20px;color:rgba(255,255,255,.75);height:30px}
.quote p{font-size:14px;line-height:25px;color:rgba(255,255,255,.6)}
.quote.main p{color:var(--white)}
.t-arrows{position:absolute;top:471px;left:555px;display:flex;gap:18px}
.t-arrows span{width:36px;height:36px;border-radius:50%;border:1.5px solid var(--white);display:flex;align-items:center;justify-content:center}

/* gallery */
.tile{position:absolute;width:214px}
.g-arrow{top:4335px}

/* footer */
.footer{top:4717px;left:0;width:1200px;height:308px;background:var(--navy-deep)}
.footer .brand{position:absolute;left:88px;top:58px;font-size:36px}
.footer .brand-dot{width:36px;height:36px}
.f-tag{position:absolute;left:88px;top:127px;width:240px;font-size:13px;line-height:20px;color:#c9cfdc}
.f-div{position:absolute;top:40px;width:1px;height:140px;background:#55607a}
.f-head{position:absolute;font-family:'Questrial',sans-serif;color:var(--white);font-size:17px;text-transform:uppercase}
.f-links{position:absolute;left:405px;font-size:11px;color:#c9cfdc;display:flex;gap:14px}
.subscribe{position:absolute;left:795px;top:116px;width:316px;height:52px;border-radius:26px;background:var(--white);border:3px solid #dfe3ea}
.subscribe span{position:absolute;left:20px;top:14px;font-size:11px;color:#aaa}
.subscribe b{position:absolute;right:3px;top:3px;width:104px;height:40px;border-radius:20px;background:var(--blue);color:var(--white);font-size:11px;font-weight:400;display:flex;align-items:center;justify-content:center}
.f-bottom{position:absolute;top:268px;font-size:11px;color:#c9cfdc}
.social{position:absolute;top:260px;display:flex;align-items:center;gap:10px;font-size:11px;color:#c9cfdc}
.social i{width:30px;height:30px;border-radius:50%;background:var(--orange);display:block}
</style>
</head>
<body>

<!-- HERO -->
<header class="hero abs">
  <svg width="1200" height="663" viewBox="0 0 1200 663" style="position:absolute;inset:0">
    <defs>
      <linearGradient id="heroWave" x1="0" y1="1" x2="1" y2="0">
        <stop offset="0" stop-color="#b8323b"/>
        <stop offset="0.55" stop-color="#d06a3a"/>
        <stop offset="1" stop-color="#de9a3c"/>
      </linearGradient>
    </defs>
    <rect width="1200" height="663" fill="#1c2a4c"/>
    <path d="M0 640 C250 660 430 560 700 470 C900 400 1060 380 1200 340 L1200 663 L0 663Z" fill="url(#heroWave)"/>
    <path d="M0 650 C280 690 500 600 760 585 C960 575 1100 620 1200 670 L1200 663 L0 663Z" fill="#ffffff"/>
  </svg>
  <nav class="nav abs">
    <div class="brand"><span class="brand-dot"></span>zKarvel</div>
    <div class="nav-links">
      <span class="active">Home</span><span>About Us</span><span>Store</span><span>Setup</span><span>Testimonials</span><span>Contact</span>
    </div>
    <svg class="abs" style="left:1106px;top:8px" width="20" height="18" viewBox="0 0 20 18" fill="none" stroke="#fff" stroke-width="1.5"><path d="M1 2h3l2 10h10l2-7H5"/><circle cx="8" cy="15" r="1.2"/><circle cx="15" cy="15" r="1.2"/></svg>
  </nav>
  <h1 class="abs">Control your gas fireplace or<br>gas wall heater with your smart<br>phone or device</h1>
  <div class="hero-btn abs">CHECK OUT OUR PRODUCT
    <svg width="18" height="12" viewBox="0 0 18 12" fill="none" stroke="#fff" stroke-width="1.6"><path d="M1 6h15M11 1l5 5-5 5"/></svg>
  </div>
  <div class="abs" role="img" aria-label="Smartphone showing the app's Add a Device screen" style="left:800px;top:195px;width:180px;height:440px;border-radius:28px;background:linear-gradient(160deg,#20325a 0%,#27407a 45%,#c9553a 75%,#d98a3a 100%);transform:rotate(10deg);border:6px solid #222"></div>
</header>

<!-- ABOUT -->
<section>
  <svg class="abs" style="left:125px;top:770px" width="520" height="520" viewBox="0 0 520 520">
    <defs>
      <linearGradient id="arc" x1="0" y1="0" x2="0" y2="1">
        <stop offset="0" stop-color="#d6a83c"/><stop offset="1" stop-color="#b9363a"/>
      </linearGradient>
    </defs>
    <path d="M300 4 A240 240 0 1 0 300 500" fill="none" stroke="url(#arc)" stroke-width="10"/>
  </svg>
  <div class="abs" role="img" aria-label="Photo of the founders assembling controller devices at a table" style="left:165px;top:793px;width:465px;height:465px;border-radius:50%;background:linear-gradient(135deg,#c8b59a,#6d6a63 60%,#3a3a3a)"></div>
  <div class="about-text abs">
    <div class="eyebrow">Who we are</div>
    <h2 class="section-title">About Us</h2>
    <p class="copy">After years in the gas fireplace industry, we had an idea. What if there was a way to control your gas fireplace or gas heating system with your smart phone? There are remotes out there that can do this, but who wants another remote control sitting on their coffee table!</p>
    <p class="copy">It took us a few years, but we finally worked out the bugs. Our innovative technology allows you to bring your gas fireplace, or even your dated gas heating system, into the 21st century.</p>
    <span class="btn-outline">Learn More</span>
  </div>
</section>

<!-- PRODUCTS -->
<section>
  <div class="center-head abs" style="top:1398px">
    <div class="eyebrow">What we offer</div>
    <h2 class="section-title" style="margin-top:6px">Our Products</h2>
    <div class="rule"></div>
  </div>
  <div class="product abs" style="left:302px;top:1531px">
    <div class="thumb placeholder" role="img" aria-label="Controller device in its black case, fireplace version" style="background:linear-gradient(135deg,#e2e2e2,#2a2a2a 55%,#111)"><span class="heart"></span></div>
    <div class="name">HearthLink - Gas Fireplaces</div>
    <div class="price">$119.00</div>
  </div>
  <div class="product abs" style="left:615px;top:1531px">
    <div class="thumb placeholder" role="img" aria-label="Open controller cases on a wooden table, wall heater version" style="background:linear-gradient(135deg,#9a8a77,#3a3838 55%,#7a6a58)"><span class="heart"></span></div>
    <div class="name">HearthLink - Gas Wall Heaters</div>
    <div class="price">$119.00</div>
  </div>
  <div class="dots abs"><i></i><i></i></div>
</section>

<!-- HOW IT WORKS -->
<section>
  <svg class="abs" style="left:0;top:2030px" width="1200" height="645" viewBox="0 0 1200 645">
    <defs>
      <linearGradient id="howLine" x1="0" x2="1">
        <stop offset="0" stop-color="#b9363a"/><stop offset="1" stop-color="#d6a83c"/>
      </linearGradient>
    </defs>
    <path d="M4 65 C250 120 600 110 900 70 C1030 55 1120 60 1200 75 L1200 645 L4 645Z" fill="#e5e6ea"/>
    <path d="M240 105 C520 90 760 60 960 45 C1080 38 1150 50 1200 70" fill="none" stroke="url(#howLine)" stroke-width="8"/>
  </svg>
  <div class="abs" role="img" aria-label="Smartphone showing the app's temperature control and countdown timer" style="left:712px;top:2028px;width:252px;height:520px;border-radius:36px;background:linear-gradient(160deg,#ffffff 0%,#f3e0c8 45%,#e88f66 75%,#d9745a 100%);border:8px solid #d9c3bd;transform:rotate(4deg)"></div>
  <div class="how-text abs">
    <div class="eyebrow">What we do</div>
    <h2 class="section-title">How It Works</h2>
    <p class="copy">Lorem ipsum dolor sit amet, consectetur adipiscing elit, sed do eiusmod tempor incididunt ut labore et dolore magna aliqua. Ut enim ad minim veniam, quis nostrud exercitation ullamco laboris nisi ut aliquip ex ea commodo consequat. Duis aute irure dolor in reprehenderit in voluptate velit esse cillum dolore eu fugiat nulla pariatur.</p>
    <div class="stores">
      <span class="store-badge" role="img" aria-label="App store download badge"></span>
      <span class="store-badge" role="img" aria-label="Android store download badge"></span>
    </div>
  </div>
</section>

<!-- SETUP -->
<section>
  <div class="video abs" role="img" aria-label="Setup video: installing the hardware">
    <span class="play"></span>
    <div class="video-caption">Set Up: The Hardware</div>
  </div>
  <div class="setup-text abs">
    <h2 class="section-title">Setting up the<br>hardware</h2>
    <div class="rule"></div>
    <p class="copy">Lorem ipsum dolor sit amet, consectetur adipiscing elit, sed do eiusmod tempor incididunt ut labore et dolore magna aliqua. Ut enim ad minim veniam, quis nostrud exercitation ullamco laboris nisi ut aliquip ex ea commodo consequat. Duis aute irure dolor in reprehenderit in voluptate velit esse cillum dolore eu fugiat nulla pariatur.</p>
    <span class="btn-outline">Learn More</span>
  </div>
</section>

<!-- TESTIMONIALS -->
<section class="testimonials abs">
  <div class="center-head abs" style="top:72px">
    <div class="eyebrow">What our clients say</div>
    <h2 class="section-title" style="margin-top:6px">Testimonials</h2>
    <div class="rule"></div>
  </div>
  <div class="quote" style="left:110px">
    <div class="mark">&ldquo;</div>
    <p>Lorem ipsum dolor sit amet, consectetur adipiscing elit, sed do eiusmod tempor incididunt ut labore et dolore magna aliqua. Ut enim ad minim veniam, quis nostrud exercitation ullamco laboris nisi ut aliquip ex ea commodo consequat.</p>
  </div>
  <div class="quote main" style="left:470px">
    <div class="mark" style="color:#fff">&ldquo;</div>
    <p>Lorem ipsum dolor sit amet, consectetur adipiscing elit, sed do eiusmod tempor incididunt ut labore et dolore magna aliqua. Ut enim ad minim veniam, quis nostrud exercitation ullamco laboris nisi ut aliquip ex ea commodo consequat. Duis aute irure dolor in reprehenderit</p>
  </div>
  <div class="quote" style="left:833px">
    <div class="mark">&ldquo;</div>
    <p>Lorem ipsum dolor sit amet, consectetur adipiscing elit, sed do eiusmod tempor incididunt ut labore et dolore magna aliqua. Ut enim ad minim veniam, quis nostrud exercitation ullamco laboris nisi ut aliquip ex ea commodo</p>
  </div>
  <div class="t-arrows">
    <span><svg width="10" height="14" viewBox="0 0 10 14" fill="none" stroke="#fff" stroke-width="1.8"><path d="M8 1L2 7l6 6"/></svg></span>
    <span><svg width="10" height="14" viewBox="0 0 10 14" fill="none" stroke="#fff" stroke-width="1.8"><path d="M2 1l6 6-6 6"/></svg></span>
  </div>
</section>

<!-- GALLERY -->
<section>
  <div class="center-head abs" style="top:3966px">
    <div class="eyebrow">How it's going on</div>
    <h2 class="section-title" style="margin-top:6px">Our Gallery</h2>
    <div class="rule"></div>
  </div>
  <svg class="abs g-arrow" style="left:110px" width="14" height="22" viewBox="0 0 14 22" fill="none" stroke="#222" stroke-width="2"><path d="M11 2L3 11l8 9"/></svg>
  <svg class="abs g-arrow" style="left:1077px" width="14" height="22" viewBox="0 0 14 22" fill="none" stroke="#222" stroke-width="2"><path d="M3 2l8 9-8 9"/></svg>
  <div class="tile" role="img" aria-label="Circuit boards laid out on a workbench" style="left:157px;top:4097px;height:198px;background:linear-gradient(135deg,#8a7a66,#4e7a6a)"></div>
  <div class="tile" role="img" aria-label="Team member working near a window" style="left:157px;top:4306px;height:289px;background:linear-gradient(160deg,#d8d2c8,#6a5f55)"></div>
  <div class="tile" role="img" aria-label="3D printer producing device cases" style="left:380px;top:4097px;height:292px;background:linear-gradient(150deg,#6a5a4a,#2d2a28)"></div>
  <div class="tile" role="img" aria-label="Bundles of wiring on a table" style="left:380px;top:4400px;height:195px;background:linear-gradient(150deg,#c2b9ae,#3f6e8a)"></div>
  <div class="tile" role="img" aria-label="Boxes of assembled boards" style="left:604px;top:4097px;height:198px;background:linear-gradient(150deg,#b84a3a,#3a6a5a)"></div>
  <div class="tile" role="img" aria-label="Soldering and assembly work at the desk" style="left:604px;top:4306px;height:289px;background:linear-gradient(150deg,#4a4844,#8a7a66)"></div>
  <div class="tile" role="img" aria-label="Founders testing a controller at home" style="left:828px;top:4097px;height:294px;background:linear-gradient(150deg,#c8b59a,#4a4a4a)"></div>
  <div class="tile" role="img" aria-label="Printing and assembly workstation" style="left:828px;top:4402px;height:193px;background:linear-gradient(150deg,#d8d8d8,#3a3a3a)"></div>
</section>

<!-- FOOTER -->
<footer class="footer abs">
  <div class="brand"><span class="brand-dot"></span>zKarvel</div>
  <p class="f-tag">Control your gas fireplace or gas wall heater with your smart phone or device</p>
  <span class="f-div" style="left:363px"></span>
  <span class="f-div" style="left:753px"></span>
  <div class="f-head" style="left:405px;top:64px">Quick Links</div>
  <div class="f-links" style="top:128px"><span>About Us</span><span>Store</span><span>Setup</span><span>Testimonials</span><span>Contact</span></div>
  <div class="f-links" style="top:158px"><span>Terms &amp; Conditions</span><span>FAQs</span><span>Privacy Policy</span></div>
  <div class="f-head" style="left:806px;top:66px">Get in touch with us</div>
  <div class="subscribe"><span>Enter your email</span><b>SUBSCRIBE</b></div>
  <div class="f-bottom" style="left:130px">© 2023 by Emberline Inc.</div>
  <div class="social" style="left:871px"><i></i>Email</div>
  <div class="social" style="left:970px"><i></i>Social</div>
</footer>

</body>
</html>
```